Career Counselor in need of a business card design

Hello Creatives! I'm in need of a business card design for a new company based in Georgia, USA called Pathways By Lumen.

Some things that may be helpful in creating your concept(s) include:

My Logo (Included in the Files section): There are three versions, two versions are in the second file. The all gold stacked (vertical) version is my primary logo and then there are two horizontal versions (one is all gold and the other is gold and grey).

My mission: to empower tweens through young adults to realize and actualize their CAREER ASPIRATIONS.
My vision: for tweens through young adults to LIVE LIFE ON PURPOSE and become CONTRIBUTING MEMBERS OF SOCIETY.

Biblical scriptures that support my ‘Why’: Psalms 127: 3-4(NIV) Children are a heritage from the Lord, offspring a reward from him. Like ARROWS in the hands of a warrior are children…. And Proverbs 29:18(JKV) Where there is no VISION, the people perish.

*Words in ALL CAPS are to emphasize what's important to me and may possibly provide you some inspiration (IDK - Have fun with it)!

Target Market(s)

My ideal customers are parents, guardians, and young adults.

Contact Information for Business Card

My name, degrees and credential: Delmira Fosket, M.S., Ed.S., NCC
Title: College and Career Coach and Consultant

Number: 555.317.8842
Address: 2618 Velbrook Avenue., Suite 407, Macon, GA 31299
Email: info@pathwaysbylumen.co
Website: www.pathwaysbylumen.co

My population: TWEENS • TEENS • EMERGING ADULTS
Services offered: One-On-One Sessions • Small Groups • Workshops

Colors

Designer to choose colors to be used in the design.

Requirements
Nice to have
• Either my mission or vision but I will understand if it does not all fit.
• My mission: To empower tweens through young adults to realize and actualize their career aspirations.
• My vision: For tweens through young adults to live life on purpose and become contributing members of society.

```html
<!DOCTYPE html>
<html lang="en">
<head>
<meta charset="utf-8">
<title>Pathways By Lumen — Business Card</title>
<link rel="stylesheet" href="https://fonts.googleapis.com/css2?family=Cinzel:wght@500&family=Pathway+Gothic+One&display=swap">
<style>
  :root {
    --page: #ececec;
    --card-dark: #222222;
    --card-light: #ffffff;
    --gold: #c9a033;
    --gold-faint: rgba(201, 160, 51, 0.12);
    --ink: #1e1e1e;
    --ink-soft: #333333;
  }
  * { margin: 0; padding: 0; box-sizing: border-box; }
  html, body { width: 1200px; height: 1200px; overflow: hidden; }
  body { background: var(--page); position: relative; font-family: "Pathway Gothic One", sans-serif; }

  .card { position: absolute; left: 282px; width: 696px; height: 416px; border-radius: 14px; overflow: hidden; }
  .card--front { top: 106px; background: var(--card-dark); }
  .card--back { top: 636px; background: var(--card-light); }

  .front__decor { position: absolute; inset: 0; }
  .front__mark { position: absolute; left: 105px; top: 130px; }
  .front__divider { position: absolute; left: 263px; top: 128px; width: 2px; height: 144px; background: var(--gold); }
  .wordmark { font-family: "Cinzel", serif; font-weight: 500; line-height: 1; }
  .wordmark__main { display: block; }
  .wordmark__sub { display: block; }
  .front__wordmark { position: absolute; left: 282px; top: 150px; color: var(--gold); }
  .front__wordmark .wordmark__main { font-size: 64px; letter-spacing: 1px; }
  .front__wordmark .wordmark__sub { font-size: 33px; letter-spacing: 8px; margin-top: 4px; }
  .front__services { position: absolute; left: 0; right: 0; top: 372px; text-align: center; color: var(--gold); font-size: 13px; letter-spacing: 0.8px; }

  .back__wordmark { position: absolute; left: 54px; top: 60px; color: var(--ink); }
  .back__wordmark .wordmark__main { font-size: 54px; letter-spacing: 1px; }
  .back__wordmark .wordmark__sub { font-size: 28px; letter-spacing: 7px; margin-top: 2px; }
  .back__mission { position: absolute; left: 38px; width: 340px; top: 176px; text-align: center; color: var(--ink-soft); font-size: 15.5px; line-height: 25px; letter-spacing: 0.6px; }
  .back__mark { position: absolute; left: 426px; top: 92px; }

  .person { position: absolute; left: 48px; top: 284px; width: 318px; }
  .person__name { font-size: 19px; color: var(--ink); letter-spacing: 0.6px; }
  .person__title { font-size: 15.5px; color: var(--ink-soft); letter-spacing: 0.6px; padding-bottom: 3px; border-bottom: 1.5px solid #555; }
  .contacts { list-style: none; margin-top: 9px; }
  .contacts__item { display: flex; align-items: center; gap: 9px; font-size: 13.5px; color: var(--ink-soft); letter-spacing: 0.6px; height: 22.5px; }
  .contacts__icon { width: 13px; height: 13px; flex: none; fill: var(--ink); }

  .back__band { position: absolute; left: 0; bottom: 0; width: 696px; height: 30px; }
  .back__site { position: absolute; right: 32px; bottom: 7px; color: #fff; font-size: 13.5px; letter-spacing: 1.4px; }
</style>
</head>
<body>

<section class="card card--front" aria-label="Card front">
  <svg class="front__decor" width="696" height="416" aria-hidden="true">
    <circle cx="498" cy="206" r="206" fill="none" stroke="var(--gold-faint)" stroke-width="34"/>
  </svg>
  <svg class="front__mark" width="140" height="140" aria-hidden="true">
    <circle cx="70" cy="70" r="66" fill="none" stroke="var(--gold)" stroke-width="6"/>
  </svg>
  <div class="front__divider"></div>
  <h1 class="wordmark front__wordmark">
    <span class="wordmark__main">PATHWAYS</span>
    <span class="wordmark__sub">BY LUMEN</span>
  </h1>
  <p class="front__services">One-On-One Sessions ▪ Small Groups ▪ Workshops</p>
</section>

<section class="card card--back" aria-label="Card back">
  <h2 class="wordmark back__wordmark">
    <span class="wordmark__main">PATHWAYS</span>
    <span class="wordmark__sub">BY LUMEN</span>
  </h2>
  <p class="back__mission">Empower Tweens Through Young Adults To Realize And Actualize Their Career Aspirations.</p>
  <svg class="back__mark" width="220" height="220" aria-hidden="true">
    <circle cx="110" cy="110" r="102" fill="none" stroke="var(--ink)" stroke-width="10"/>
  </svg>

  <div class="person">
    <p class="person__name">Delmira Fosket, M.S., Ed.S., NCC</p>
    <p class="person__title">College and Career Coach and Consultant</p>
    <ul class="contacts">
      <li class="contacts__item">
        <svg class="contacts__icon" viewBox="0 0 24 24" aria-hidden="true"><path d="M6.6 10.8a15.1 15.1 0 0 0 6.6 6.6l2.2-2.2c.3-.3.7-.4 1-.2 1.1.4 2.3.6 3.6.6.6 0 1 .4 1 1V20c0 .6-.4 1-1 1A17 17 0 0 1 3 4c0-.6.4-1 1-1h3.5c.6 0 1 .4 1 1 0 1.3.2 2.5.6 3.6.1.3 0 .7-.2 1z"/></svg>
        555.317.8842
      </li>
      <li class="contacts__item">
        <svg class="contacts__icon" viewBox="0 0 24 24" aria-hidden="true"><path d="M2 5h20v2l-10 6L2 7z"/><path d="M2 9l10 6 10-6v10H2z"/></svg>
        info@pathwaysbylumen.co
      </li>
      <li class="contacts__item">
        <svg class="contacts__icon" viewBox="0 0 24 24" aria-hidden="true"><path d="M12 1a8 8 0 0 0-8 8c0 6 8 14 8 14s8-8 8-14a8 8 0 0 0-8-8zm0 11a3 3 0 1 1 0-6 3 3 0 0 1 0 6z"/></svg>
        2618 Velbrook Avenue., Suite 407, Macon, GA 31299
      </li>
    </ul>
  </div>

  <svg class="back__band" viewBox="0 0 696 30" aria-hidden="true">
    <rect x="0" y="26" width="696" height="4" fill="var(--ink)"/>
    <path d="M470 30 C 478 30, 482 6, 496 6 L 696 6 L 696 30 Z" fill="var(--ink)"/>
  </svg>
  <p class="back__site">www.pathwaysbylumen.co</p>
</section>

</body>
</html>
```